7 3/4 x 5 1/4 Annual Banquet Invitation

Design an invitation for our Chamber's annual banquet. It will be a single sided invitation 5 1/4" wide by 7 3/4" height that we will print in-house. Our logo is attached. The theme is "Serving Together". I was thinking of an image with two hands coming together in a handshake, perhaps intertwining our logo colors. This is just a thought. I am open for any suggestions! Text for the invitation should be as follows: The Board of Directors and Staff cordially invites you to attend the 64th Yearly Gathering & Micro-Trade Fair - Monday, January 22, 2018. 5:30 p.m. Social, 6:00 p.m. Dinner. Cedarvale Chapel, 4819 Harlan P. Moss Rd S, Fernbrook. Please RSVP by January 18, 2018.

Target Market(s)

This invitation will be printed and mailed to our membership.

Industry/Entity Type

Business Management

Colors
33a6d7
faa54b
0355a3
00a990

Requirements
Must have
• Event info as indentified above.
Nice to have
• Our Logo

```html
<!DOCTYPE html>
<html lang="en">
<head>
<meta charset="utf-8">
<title>Serving Together – Annual Banquet Invitation</title>
<link rel="stylesheet" href="https://fonts.googleapis.com/css2?family=Montserrat:wght@500;600;700;800;900&display=swap">
<style>
  :root {
    --backdrop: #d9d6d2;
    --card-orange: #f7a845;
    --grunge: rgba(120, 80, 30, 0.35);
    --ink-blue: #2b3a9c;
    --panel: rgba(255, 236, 210, 0.62);
    --badge-orange: #f59220;
    --bar-black: #1b1b1b;
    --white: #ffffff;
  }
  * { margin: 0; padding: 0; box-sizing: border-box; }
  html, body {
    width: 1200px;
    height: 1192px;
    overflow: hidden;
    background: var(--backdrop);
    font-family: "Montserrat", sans-serif;
  }
  .invitation {
    position: absolute;
    left: 210px;
    top: 21px;
    width: 779px;
    height: 1150px;
    overflow: hidden;
    background:
      radial-gradient(ellipse at 0% 0%, var(--grunge), transparent 45%),
      radial-gradient(ellipse at 100% 20%, var(--grunge), transparent 40%),
      radial-gradient(ellipse at 0% 100%, var(--grunge), transparent 40%),
      radial-gradient(ellipse at 100% 100%, rgba(120, 80, 30, 0.25), transparent 35%),
      var(--card-orange);
  }
  .hands-art { position: absolute; }
  .hands-art--reaching {
    left: 0;
    top: 90px;
    width: 270px;
    height: 360px;
    border-radius: 0 60% 60% 0;
    background: linear-gradient(135deg, rgba(43, 58, 156, 0.55), rgba(43, 58, 156, 0.15));
  }
  .hands-art--raised {
    left: 340px;
    top: 600px;
    width: 439px;
    height: 550px;
    border-radius: 60% 0 0 0;
    background: linear-gradient(200deg, rgba(43, 58, 156, 0.95), rgba(43, 58, 156, 0.55));
  }
  .theme-title {
    position: absolute;
    top: 143px;
    width: 100%;
    text-align: center;
    color: var(--ink-blue);
    font-weight: 700;
    font-size: 37px;
    line-height: 34px;
    letter-spacing: -0.5px;
  }
  .info-panel {
    position: absolute;
    left: 186px;
    top: 232px;
    width: 407px;
    height: 774px;
    background: var(--panel);
    text-align: center;
    color: var(--ink-blue);
  }
  .invite-line {
    margin-top: 52px;
    font-size: 16.5px;
    font-weight: 600;
    line-height: 18px;
    color: var(--bar-black);
  }
  .event-name {
    position: relative;
    z-index: 2;
    margin-top: 6px;
    font-size: 44px;
    font-weight: 900;
    line-height: 37px;
    letter-spacing: -2px;
    text-transform: uppercase;
  }
  .date-badge {
    position: absolute;
    z-index: 1;
    left: 106px;
    top: 355px;
    width: 196px;
    height: 196px;
    border-radius: 50%;
    background: var(--badge-orange);
    color: var(--white);
    font-weight: 700;
    font-size: 22px;
    line-height: 24px;
    display: flex;
    align-items: center;
    justify-content: center;
    text-align: center;
    padding-bottom: 8px;
  }
  .event-details {
    position: absolute;
    z-index: 2;
    top: 513px;
    width: 100%;
    font-size: 16.5px;
    font-weight: 700;
    line-height: 21px;
    letter-spacing: 0.3px;
  }
  .rsvp-bar {
    position: absolute;
    left: 45px;
    top: 600px;
    width: 316px;
    height: 21px;
    background: var(--bar-black);
    color: var(--white);
    font-size: 13.5px;
    font-weight: 600;
    line-height: 21px;
  }
  .organiser {
    position: absolute;
    top: 650px;
    width: 100%;
  }
  .organiser-dot {
    display: block;
    width: 50px;
    height: 50px;
    margin: 0 auto 22px;
    border-radius: 50%;
    background: var(--badge-orange);
  }
  .organiser-name {
    font-size: 19px;
    font-weight: 700;
    line-height: 20px;
  }
  .organiser-sub {
    font-size: 10.5px;
    font-weight: 500;
    letter-spacing: 3px;
    line-height: 13px;
  }
</style>
</head>
<body>
  <main class="invitation">
    <div class="hands-art hands-art--reaching" role="img" aria-label="Line drawing of a blue hand reaching in from the upper left"></div>
    <div class="hands-art hands-art--raised" role="img" aria-label="Drawing of several blue hands raised up from the lower right"></div>

    <h1 class="theme-title">SERVING<br>TOGETHER</h1>

    <section class="info-panel">
      <p class="invite-line">THE BOARD OF DIRECTORS<br>AND STAFF CORDIALLY INVITES<br>YOU TO ATTEND</p>
      <h2 class="event-name">The 64th<br>Yearly<br>Gathering<br>&amp;<br>Micro-<br>Trade<br>Fair.</h2>

      <div class="date-badge">MONDAY,<br>JANUARY 22,<br>2018.</div>

      <p class="event-details">5:30 P.M. SOCIAL, 6:00 P.M.<br>DINNER - CEDARVALE CHAPEL,<br>4819 HARLAN P. MOSS RD S,<br>FERNBROOK.</p>

      <p class="rsvp-bar">PLEASE RSVP BY JANUARY 18, 2018.</p>

      <div class="organiser">
        <span class="organiser-dot"></span>
        <p class="organiser-name">HARBORLINE CHAMBER</p>
        <p class="organiser-sub">OF COMMERCE &amp; TOURISM</p>
      </div>
    </section>
  </main>
</body>
</html>
```